Update Business Card Design

I'm looking to update my business cards. Attached is a photo of the current design. I like the black side so that does not have to be update. The white side needs to be updated. I want the design to be modern and minimalistic.
I am a lawyer and my firm's website is www.harborstonepartners.com (for reference).
My firm's logo has a horizontal version (which is on the black side of the card) and a vertical version (on the white side). I would prefer to keep the vertical version on the white side and horizontal version on the black side (the logo files are attached).

I am open to redesigning the black side also. I would like one side to have the horizontal logo and the other to have the vertical logo.

Went on vacation/holiday

```html
<!DOCTYPE html>
<html lang="en">
<head>
<meta charset="utf-8">
<title>Harborstone Partners – Business Cards</title>
<link rel="stylesheet" href="https://fonts.googleapis.com/css2?family=Montserrat:wght@400;500;600;700&display=swap">
<style>
  :root {
    --page: #151515;
    --card: #252525;
    --accent: #12b5dc;
    --ink: #ffffff;
    --soft: #e8e8e8;
  }
  * { margin: 0; padding: 0; box-sizing: border-box; }
  html, body {
    width: 1200px; height: 1059px; overflow: hidden;
    background: var(--page);
    font-family: "Montserrat", sans-serif;
    color: var(--ink);
  }
  .canvas { position: relative; width: 1200px; height: 1059px; }
  .card {
    position: absolute;
    background: var(--card);
    border-radius: 20px;
    overflow: hidden;
  }
  .card--front { left: 256px; top: 89px; width: 688px; height: 390px; }
  .card--back  { left: 254px; top: 547px; width: 693px; height: 393px; }

  .brand {
    position: absolute; left: 0; right: 0;
    display: flex; align-items: center; justify-content: center;
  }
  .brand__square { background: var(--accent); flex: none; }
  .brand__name {
    color: var(--accent);
    font-weight: 600;
    text-transform: uppercase;
    letter-spacing: 0.04em;
    line-height: 1.05;
  }
  .card--front .brand { top: 62px; gap: 18px; }
  .card--front .brand__square { width: 26px; height: 26px; }
  .card--front .brand__name { font-size: 30px; }
  .card--back .brand { top: 140px; gap: 24px; }
  .card--back .brand__square { width: 36px; height: 36px; }
  .card--back .brand__name { font-size: 42px; }

  .person {
    position: absolute; right: 365px; top: 218px;
    text-align: right;
  }
  .person__name { color: var(--accent); font-weight: 700; font-size: 21px; letter-spacing: 0.02em; line-height: 24px; }
  .person__title { font-size: 15px; line-height: 22px; color: var(--soft); letter-spacing: 0.02em; }
  .person__mobile { font-size: 15px; line-height: 22px; margin-top: 3px; color: var(--soft);
    display: flex; align-items: center; justify-content: flex-end; gap: 5px; }

  .rule { position: absolute; left: 344px; top: 210px; width: 1px; height: 79px; background: var(--accent); }

  .contacts { position: absolute; left: 364px; top: 206px; list-style: none; }
  .contacts li {
    display: flex; align-items: center; gap: 7px;
    font-size: 15px; line-height: 21.5px; color: var(--soft); letter-spacing: 0.02em;
  }
  .contacts svg { width: 13px; height: 13px; flex: none; }

  .address-band {
    position: absolute; left: 0; right: 0; top: 324px; height: 29px;
    background: var(--accent);
    display: flex; align-items: center; justify-content: center;
    font-size: 15px; letter-spacing: 0.03em; color: var(--ink);
  }

  .site {
    position: absolute; left: 0; right: 0; top: 342px;
    text-align: center; font-size: 15px; letter-spacing: 0.18em; color: var(--ink);
  }
  .site__domain { color: var(--accent); }
</style>
</head>
<body>
<main class="canvas">

  <section class="card card--front" aria-label="Card front">
    <div class="brand">
      <span class="brand__square"></span>
      <span class="brand__name">Harborstone<br>Partners</span>
    </div>

    <div class="person">
      <p class="person__name">DANIEL REYES</p>
      <p class="person__title">Attorney at Law</p>
      <p class="person__mobile">310.555.0196
        <svg width="10" height="14" viewBox="0 0 10 14" aria-hidden="true"><rect x="1" y="0.8" width="8" height="12.4" rx="1.5" fill="none" stroke="var(--accent)" stroke-width="1.4"/><circle cx="5" cy="10.8" r="0.9" fill="var(--accent)"/></svg>
      </p>
    </div>

    <span class="rule"></span>

    <ul class="contacts">
      <li><svg viewBox="0 0 16 16" aria-hidden="true"><path d="M3.5 1.5l2.3 2.6-1.2 1.6c.8 1.9 2.2 3.4 4.2 4.4l1.5-1.3 2.7 2.3-1.3 2.1C7 13 2.9 8.9 2 3.1z" fill="var(--accent)"/></svg>310.555.0142</li>
      <li><svg viewBox="0 0 16 16" aria-hidden="true"><rect x="4" y="1" width="8" height="4" fill="var(--accent)"/><rect x="1" y="6" width="14" height="6" rx="1" fill="var(--accent)"/><rect x="4" y="10" width="8" height="5" fill="var(--accent)" stroke="var(--card)" stroke-width="1"/></svg>310.555.0178</li>
      <li><svg viewBox="0 0 16 16" aria-hidden="true"><rect x="1" y="3" width="14" height="10" fill="var(--accent)"/><path d="M1 3l7 6 7-6" fill="none" stroke="var(--card)" stroke-width="1.2"/></svg>daniel@HarborstonePartners.com</li>
      <li><svg viewBox="0 0 16 16" aria-hidden="true"><g fill="none" stroke="var(--accent)" stroke-width="1.2"><circle cx="8" cy="8" r="6.5"/><ellipse cx="8" cy="8" rx="3" ry="6.5"/><path d="M1.5 8h13M2.5 4.8h11M2.5 11.2h11"/></g></svg>www.harborstonepartners.com</li>
    </ul>

    <div class="address-band">1150 Marlowe Avenue, Suite 204 Westfield, CA 90218</div>
  </section>

  <section class="card card--back" aria-label="Card back">
    <div class="brand">
      <span class="brand__square"></span>
      <span class="brand__name">Harborstone<br>Partners</span>
    </div>
    <p class="site">www.<span class="site__domain">harborstonepartners</span>.com</p>
  </section>

</main>
</body>
</html>
```